Data analytics company needs a website banner design

We need an image for our website's slider. Our website uses the Tessara template from PixVault (https://pixvault.example/site-theme/tessara/). We are a data analytics company that develops real-time process monitoring software for manufacturing. Our initial product, FlowSense, relies upon AI and machine learning algorithms to provide fault and anomaly detection for manufacturing process health. We would like to see designs that (a) incorporate some of the following concepts, AI, pattern recognition, digital transformation (1s and 0s), machine learning, health, etc., and (b) illustrate a screenshot of our software superimposed on a large desktop flat screen monitor. The focus should be on the screenshot on the monitor, while the other concepts (1s and 0s etc) should be subtle (potentially fading out from left to right) with the monitor on the right. It would be nice if I could swap out the screenshot once the design is complete. An example screenshot is provided in the Upload Files. Different resolutions and ratios of the screenshot can be generated if necessary.
Look and feel
Each slider illustrates characteristics of the customer's brand and the style your logo design should communicate.

```html
<!DOCTYPE html>
<html lang="en">
<head>
<meta charset="utf-8">
<title>FlowSense – Data analytics banner</title>
<link rel="stylesheet" href="https://fonts.googleapis.com/css2?family=Montserrat:wght@500;600&family=Open+Sans:wght@600&family=Roboto:wght@300;400&family=Libre+Franklin:wght@800&display=swap">
<style>
  :root {
    --page-top: #ffffff;
    --page-bottom: #ececec;
    --navy-deep: #040c33;
    --navy: #0a2a7a;
    --blue-bright: #1d5fd0;
    --accent: #62c3f1;
    --digit: #8cc4ff;
    --white: #ffffff;
    --ink: #222222;
    --rule-rose: #c9a0a4;
    --bezel: #161616;
    --chin: #d6d6d6;
    --stand: #bdbdbd;
  }
  * { margin: 0; padding: 0; box-sizing: border-box; }
  html, body { width: 1017px; height: 1200px; overflow: hidden; background: var(--page-bottom); }
  .canvas { position: relative; width: 1017px; height: 1200px; overflow: hidden; }
  .page-top { position: absolute; left: 0; top: 0; width: 1017px; height: 640px; background: var(--page-top); }

  /* Banner */
  .banner { position: absolute; overflow: hidden; }
  .banner--lead { left: 24px; top: 17px; width: 972px; height: 415px; }
  .banner--alt  { left: 51px; top: 719px; width: 919px; height: 394px; }
  .banner-backdrop {
    position: absolute; inset: 0;
    background:
      radial-gradient(ellipse at 45% 80%, rgba(90,160,255,0.35) 0%, rgba(90,160,255,0) 45%),
      linear-gradient(90deg, rgba(4,12,51,0.55) 0%, rgba(4,12,51,0) 50%),
      linear-gradient(100deg, var(--navy-deep) 0%, var(--navy) 45%, var(--blue-bright) 100%);
  }
  .binary-digits { position: absolute; inset: 0; width: 100%; height: 100%; }
  .binary-digits text { font-family: 'Montserrat', sans-serif; font-weight: 500; fill: var(--digit); }

  .brand { position: absolute; display: flex; align-items: center; gap: 16px; }
  .banner--lead .brand { left: 56px; top: 38px; }
  .banner--alt .brand  { left: 55px; top: 35px; }
  .brand-mark { width: 66px; height: 66px; border-radius: 50%; background: var(--white); opacity: .9; flex: none; }
  .brand-name {
    font-family: 'Montserrat', sans-serif; font-weight: 500; font-size: 30px;
    color: var(--white); letter-spacing: 2px; line-height: 1;
  }
  .brand-tagline {
    font-family: 'Montserrat', sans-serif; font-weight: 500; font-size: 7.5px;
    color: var(--white); letter-spacing: 2.2px; margin-top: 7px;
  }
  .headline {
    position: absolute; font-family: 'Montserrat', sans-serif; font-weight: 600;
    font-size: 42px; line-height: 1.1; color: var(--accent); letter-spacing: .5px;
  }
  .banner--lead .headline { left: 52px; top: 150px; }
  .banner--alt .headline  { left: 51px; top: 138px; }
  .intro {
    position: absolute; font-family: 'Open Sans', sans-serif; font-weight: 600;
    font-size: 15.3px; line-height: 20.9px; color: var(--white); white-space: nowrap;
  }
  .banner--lead .intro { left: 55px; top: 216px; }
  .banner--alt .intro  { left: 52px; top: 202px; font-size: 14.8px; line-height: 20px; }
  .accent-rule { position: absolute; height: 4px; background: var(--accent); }
  .banner--lead .accent-rule { left: 56px; top: 346px; width: 128px; }
  .banner--alt .accent-rule  { left: 53px; top: 329px; width: 121px; }

  /* Monitor */
  .monitor { position: absolute; }
  .monitor--lead { left: 506px; top: 38px; width: 456px; height: 436px; }
  .monitor--alt  { left: 508px; top: 737px; width: 433px; height: 414px; }
  .screen-text { font-family: 'Open Sans', sans-serif; font-weight: 600; fill: #333; }

  /* Product copy */
  .product-copy { position: absolute; left: 140px; top: 458px; width: 580px; color: var(--ink); }
  .product-title { font-family: 'Roboto', sans-serif; font-weight: 300; font-size: 35px; line-height: 1.2; letter-spacing: -.5px; }
  .product-subtitle { font-family: 'Libre Franklin', sans-serif; font-weight: 800; font-size: 23.5px; line-height: 30px; margin-top: 6px; }
  .product-rule { width: 560px; height: 2px; background: var(--rule-rose); margin-top: 14px; }
  .product-lede { font-family: 'Roboto', sans-serif; font-weight: 400; font-size: 16px; margin-top: 9px; letter-spacing: -.2px; }
  .product-lede sub { font-size: 11px; }
</style>
</head>
<body>
<div class="canvas">
  <div class="page-top"></div>

  <svg width="0" height="0" style="position:absolute">
    <defs>
      <g id="profile-chart">
        <rect x="0" y="0" width="150" height="100" fill="#fff" stroke="#999" stroke-width=".6"/>
        <polygon points="6,14 140,10 140,36 6,38" fill="#b8b8b8" opacity=".7"/>
        <polyline points="0,98 5,98 7,24 40,22 70,21 82,20 86,40 89,52 92,24 120,19 140,18 144,98 150,98" fill="none" stroke="#2b3fd6" stroke-width="1.1"/>
        <rect x="92" y="4" width="54" height="8" fill="#fff" stroke="#666" stroke-width=".4"/>
      </g>
      <g id="feature-chart">
        <rect x="0" y="0" width="150" height="100" fill="#fff" stroke="#999" stroke-width=".6"/>
        <polygon points="4,40 30,34 55,30 80,26 105,20 130,16 146,22 146,60 120,54 95,62 70,58 45,60 20,66 4,64" fill="#d6f3cc"/>
        <polyline points="4,40 18,40 18,34 40,34 40,30 62,30 62,26 84,26 84,22 106,22 106,16 128,16 128,22 146,22" fill="none" stroke="#e0463c" stroke-width="1"/>
        <polyline points="4,64 20,64 20,60 44,60 44,58 70,58 70,62 94,62 94,54 120,54 120,60 146,60" fill="none" stroke="#e0463c" stroke-width="1"/>
        <g stroke="#2b3fd6" stroke-width="1.6">
          <line x1="10" y1="52" x2="20" y2="52"/><line x1="30" y1="46" x2="40" y2="46"/>
          <line x1="52" y1="44" x2="62" y2="44"/><line x1="74" y1="48" x2="84" y2="48"/>
          <line x1="96" y1="38" x2="106" y2="38"/><line x1="118" y1="34" x2="128" y2="34"/>
        </g>
        <rect x="100" y="4" width="46" height="8" fill="#fff" stroke="#666" stroke-width=".4"/>
      </g>
      <symbol id="desktop-monitor" viewBox="0 0 460 440">
        <rect x="0" y="0" width="460" height="372" rx="14" fill="var(--bezel)"/>
        <path d="M0,340 H460 V358 a14,14 0 0 1 -14,14 H14 a14,14 0 0 1 -14,-14 Z" fill="var(--chin)"/>
        <polygon points="200,372 260,372 272,420 188,420" fill="var(--stand)"/>
        <rect x="150" y="418" width="160" height="12" rx="3" fill="#a9a9a9"/>
        <rect x="12" y="12" width="436" height="322" fill="#f4f4f4"/>
        <rect x="12" y="12" width="436" height="11" fill="#e2e2e2"/>
        <text class="screen-text" x="210" y="20" font-size="5.5">FlowSense 0.18</text>
        <rect x="12" y="23" width="436" height="15" fill="#ececec"/>
        <g fill="#5a7fbf">
          <circle cx="22" cy="31" r="3"/><circle cx="32" cy="31" r="3"/><circle cx="42" cy="31" r="3"/><circle cx="52" cy="31" r="3"/>
        </g>
        <rect x="14" y="40" width="84" height="292" fill="#fff" stroke="#ccc" stroke-width=".5"/>
        <g class="screen-text" font-size="5">
          <text x="20" y="52">Projects</text><text x="26" y="62">Sessions</text>
          <text x="32" y="72">Data</text><text x="32" y="82">Analysis</text>
          <text x="32" y="92">Features</text><text x="26" y="102">Reports</text>
        </g>
        <rect x="14" y="108" width="84" height="7" fill="#9cc97a"/>
        <rect x="14" y="290" width="84" height="42" fill="#fafafa" stroke="#ccc" stroke-width=".5"/>
        <g stroke="#ddd" stroke-width=".5">
          <line x1="14" y1="300" x2="98" y2="300"/><line x1="14" y1="310" x2="98" y2="310"/><line x1="14" y1="320" x2="98" y2="320"/>
        </g>
        <g font-size="5.5">
          <rect x="102" y="40" width="170" height="144" fill="#fff" stroke="#ccc" stroke-width=".5"/>
          <text class="screen-text" x="108" y="52">Profile Visualizer</text>
          <use href="#profile-chart" transform="translate(114,60)"/>
          <rect x="276" y="40" width="170" height="144" fill="#fff" stroke="#ccc" stroke-width=".5"/>
          <text class="screen-text" x="284" y="52">Feature Generator</text>
          <use href="#feature-chart" transform="translate(288,60)"/>
          <rect x="102" y="188" width="170" height="144" fill="#fff" stroke="#ccc" stroke-width=".5"/>
          <text class="screen-text" x="108" y="200">Profile Visualizer</text>
          <use href="#profile-chart" transform="translate(114,208)"/>
          <rect x="276" y="188" width="170" height="144" fill="#fff" stroke="#ccc" stroke-width=".5"/>
          <text class="screen-text" x="284" y="200">Feature Generator</text>
          <use href="#feature-chart" transform="translate(288,208)"/>
        </g>
      </symbol>
      <g id="digit-field">
        <text x="420" y="240" font-size="30" opacity=".35">10 1</text>
        <text x="385" y="275" font-size="26" opacity=".3">1 111</text>
        <text x="400" y="310" font-size="26" opacity=".3">1 11 0</text>
        <text x="410" y="360" font-size="24" opacity=".25">1 0 1</text>
        <text x="210" y="380" font-size="26" opacity=".18">0 1 00</text>
        <text x="20" y="395" font-size="24" opacity=".12">0 1 1 10 0 1</text>
        <text x="330" y="340" font-size="22" opacity=".2">0 1</text>
        <text x="935" y="70" font-size="28" opacity=".35">1 1</text>
        <text x="930" y="180" font-size="26" opacity=".4">101</text>
        <text x="940" y="240" font-size="24" opacity=".3">0</text>
        <text x="945" y="300" font-size="24" opacity=".3">1</text>
      </g>
    </defs>
  </svg>

  <section class="banner banner--lead">
    <div class="banner-backdrop" role="img" aria-label="Dark blue server room photo with glowing data light"></div>
    <svg class="binary-digits" aria-hidden="true"><use href="#digit-field"/></svg>
    <div class="brand">
      <span class="brand-mark"></span>
      <div>
        <div class="brand-name">FlowSense</div>
        <div class="brand-tagline">MANUFACTURING BEHAVIORAL ANALYSIS</div>
      </div>
    </div>
    <h1 class="headline">Data analytics</h1>
    <p class="intro">Our initial product, FlowSense, relies<br>upon AI and machine learning<br>algorithms to provide fault and<br>anomaly detection for manufacturing<br>process health.</p>
    <div class="accent-rule"></div>
  </section>
  <svg class="monitor monitor--lead" viewBox="0 0 460 440" aria-label="Desktop monitor showing the FlowSense monitoring software"><use href="#desktop-monitor"/></svg>

  <div class="product-copy">
    <p class="product-title">Access Control Made Easy</p>
    <p class="product-subtitle">Affordable, Scalable,<br>Browser-Based Access Control</p>
    <div class="product-rule"></div>
    <p class="product-lede">The Gateline G<sub>3</sub>-Series represents the next step in the evolution of Northway’s</p>
  </div>

  <section class="banner banner--alt">
    <div class="banner-backdrop" role="img" aria-label="Dark blue server room photo with glowing data light"></div>
    <svg class="binary-digits" aria-hidden="true"><use href="#digit-field" transform="scale(0.95)"/></svg>
    <div class="brand">
      <span class="brand-mark"></span>
      <div>
        <div class="brand-name">FlowSense</div>
        <div class="brand-tagline">MANUFACTURING BEHAVIORAL ANALYSIS</div>
      </div>
    </div>
    <h1 class="headline">Data analytics</h1>
    <p class="intro">Our initial product, FlowSense, relies<br>upon AI and machine learning<br>algorithms to provide fault and<br>anomaly detection for manufacturing<br>process health.</p>
    <div class="accent-rule"></div>
  </section>
  <svg class="monitor monitor--alt" viewBox="0 0 460 440" aria-label="Desktop monitor showing the FlowSense monitoring software"><use href="#desktop-monitor"/></svg>
</div>
</body>
</html>
```